New landing page

We have an existing design at www.hostqubit.com but we are not set on that design and probably want something different.
We want to increase conversion rates and experiment with a new landing page for our lumo bidclick campains.
We want to use a more single page long design page that contains these elements on one page:

Header
Images/headline
4 offer boxes
Features
Locations (map)
Testimonials
Why HostQubit
Footer menu

Note should also be taken of research done by Fernlatch like this:
http://fernlatch.com/landing-page-articles/the-anatomy-of-a-landing-page/

```html
<!DOCTYPE html>
<html lang="en">
<head>
<meta charset="utf-8">
<title>HostQubit – VPS Hosting</title>
<link href="https://fonts.googleapis.com/css2?family=Roboto:wght@400;500;700;900&family=Roboto+Condensed:wght@400;700&display=swap" rel="stylesheet">
<style>
:root{
  --gold:#f8b400;
  --gold-light:#fde28a;
  --gold-pale:#fff2c2;
  --gold-dark:#d99a00;
  --ink:#1d1d1d;
  --dark:#232323;
  --darker:#161616;
  --grey:#555;
  --mute:#777;
  --white:#fff;
}
*{box-sizing:border-box;margin:0;padding:0}
html,body{width:1200px;height:3130px;overflow:hidden}
body{font-family:"Roboto",Arial,sans-serif;color:var(--ink);background:var(--white);position:relative}
.abs{position:absolute}

/* header */
.site-header{position:absolute;left:0;top:0;width:1200px;height:110px;background:linear-gradient(#2b2b2b,#1b1b1b)}
.brand{position:absolute;display:flex;align-items:center;gap:12px;color:var(--white);font-weight:700;font-size:40px}
.brand-dot{width:40px;height:40px;border-radius:50%;background:var(--gold)}
.site-header .brand{left:130px;top:48px}
.top-links{position:absolute;right:130px;top:22px;display:flex;gap:22px;color:var(--white);font-size:15px;align-items:center}
.top-links span{display:flex;align-items:center;gap:6px}
.main-nav{position:absolute;right:130px;top:64px;display:flex;gap:6px;align-items:center}
.main-nav a{color:var(--white);text-decoration:none;font-weight:500;font-size:17px;padding:8px 12px;border-radius:18px}
.main-nav a.active{background:var(--gold)}

/* hero */
.hero{position:absolute;left:0;top:110px;width:1200px;height:347px;background:linear-gradient(90deg,#4f5256,#9a9da1 55%,#c4c6c9)}
.hero-photo{position:absolute;left:0;top:0;width:600px;height:347px;background:linear-gradient(100deg,#3b4046,#6c737b 50%,#9aa0a6)}
.hero-tagline{position:absolute;right:140px;top:12px;text-align:right;color:var(--white);font-size:23px;line-height:30px}
.slider-dots{position:absolute;left:642px;top:318px;display:flex;gap:10px}
.slider-dots i{width:18px;height:18px;border-radius:50%;background:var(--white);display:block}
.slider-dots i.on{background:var(--gold)}

/* testimonial band */
.quote-band{position:absolute;left:0;top:457px;width:1200px;height:104px;background:var(--gold)}
.quote-avatar{position:absolute;left:140px;top:14px;width:68px;height:66px;border:3px solid var(--white);background:linear-gradient(#c99a76,#6b4a3a)}
.quote-text{position:absolute;left:222px;top:14px;width:500px;font-size:14px;font-style:italic;line-height:19px;color:var(--ink)}
.quote-author{position:absolute;left:610px;top:66px;font-weight:700;font-size:15px;color:var(--ink)}

/* enquiry */
.enquiry{position:absolute;left:752px;top:196px;width:305px;height:477px;background:#f3f3f3;border:1px solid #cfcfcf;box-shadow:0 4px 14px rgba(0,0,0,.3);padding:76px 16px 0}
.enquiry-head{position:absolute;left:28px;top:6px;width:250px;height:50px;border-radius:6px;background:linear-gradient(var(--gold),var(--gold-dark));color:var(--white);font-weight:700;font-size:24px;text-align:center;line-height:50px}
.enquiry p{font-size:13px;line-height:17px;color:#333}
.enquiry label{display:block;font-size:13px;margin:16px 0 4px;color:#333}
.field{height:24px;border:1px solid #bbb;background:var(--white)}
.select{display:flex;justify-content:space-between;align-items:center;padding-left:6px;font-size:13px}
.select b{width:22px;height:22px;background:#ddd;display:flex;align-items:center;justify-content:center}
.submit{display:block;margin:14px auto 0;width:88px;height:32px;background:var(--gold);color:var(--white);font-weight:700;font-size:15px;text-align:center;line-height:32px;border-radius:3px}
.enquiry .foot{text-align:center;margin-top:12px}

/* section headings */
.section-title{position:absolute;left:0;width:1200px;display:flex;justify-content:center;align-items:center;gap:24px;font-weight:700;letter-spacing:1px}
.section-title::before,.section-title::after{content:"";width:130px;height:8px;border-top:2px solid currentColor;border-bottom:2px solid currentColor;opacity:.9}

/* about */
.about-title{top:618px;font-size:50px;color:var(--ink)}
.about-title::before,.about-title::after{color:var(--gold)}
.about-copy{position:absolute;left:140px;top:700px;width:920px;font-size:14px;line-height:21px;color:#333;text-align:center}
.about-list{position:absolute;left:0;top:845px;width:1200px;list-style:none;text-align:center;font-size:16px;color:#333}
.about-list li{margin-bottom:20px}
.about-list li::before{content:"";display:inline-block;width:12px;height:12px;border-radius:50%;background:#9a9a9a;margin-right:14px;vertical-align:1px}

/* services */
.services{position:absolute;left:0;top:1005px;width:1200px;height:522px;background:var(--gold)}
.services-title{top:22px;font-size:50px;color:var(--white)}
.plans{position:absolute;left:122px;top:105px;display:flex;gap:12px}
.plan{width:230px;height:390px;background:var(--gold-light);border:2px solid var(--gold-dark);text-align:center}
.plan h3{font-size:27px;font-weight:500;margin:18px 0 10px}
.plan .ram{font-size:15px;margin-bottom:16px}
.plan ul{list-style:none;font-size:15px;line-height:20px}
.plan .act{font-weight:700;margin-top:10px}
.plan-price{margin-top:14px;border-top:2px solid var(--gold-dark);background:var(--gold-pale);height:152px;padding:12px 18px 0;text-align:left}
.plan-price small{font-size:15px;display:block}
.plan-price .amt{font-size:14px}
.plan-price .amt b{font-size:38px;font-weight:500}
.order{display:block;margin-top:6px;height:38px;background:#111;color:var(--white);font-weight:700;font-size:19px;line-height:38px;text-align:center;border-radius:3px}
.plan-price .cmp{display:block;text-align:center;font-size:11px;margin-top:8px}

/* cta bar */
.cta-bar{position:absolute;left:0;top:1527px;width:1200px;height:78px;background:linear-gradient(#2a2a2a,#151515);color:var(--white)}
.cta-bar .msg{position:absolute;left:130px;top:24px;font-size:23px}
.cta-bar .phone{position:absolute;left:630px;top:24px;font-size:22px;font-weight:700;display:flex;align-items:center;gap:10px}
.cta-btn{position:absolute;left:866px;top:14px;width:204px;height:50px;background:linear-gradient(var(--gold),var(--gold-dark));border-radius:6px;text-align:center;line-height:50px;font-weight:700;font-size:24px;color:var(--white)}

/* features */
.features-title{top:1634px;font-size:50px;color:var(--ink)}
.features-title::before,.features-title::after{color:var(--gold)}
.feature-grid{position:absolute;left:90px;top:1712px;width:1020px;display:grid;grid-template-columns:repeat(3,340px);grid-template-rows:238px 232px 190px 170px}
.feature{text-align:center;padding:0 30px}
.feature svg{display:block;margin:0 auto 6px}
.feature h4{font-size:20px;font-weight:700;margin-bottom:8px;white-space:nowrap}
.feature p{font-size:14px;line-height:18px;color:var(--mute)}
.feature a{color:#1a6bc4;font-weight:700}

/* contact */
.contact{position:absolute;left:0;top:2584px;width:1200px;height:444px;background:linear-gradient(160deg,#b9b59c,#d6d0b4 40%,#a9b19a 70%,#c5bfa4)}
.contact-overlay{position:absolute;left:290px;top:0;width:640px;height:444px;background:rgba(20,20,20,.55)}
.contact h2{position:absolute;left:0;top:14px;width:1200px;text-align:center;color:var(--white);font-weight:500;font-size:26px}
.close{position:absolute;left:920px;top:16px;width:36px;height:36px;border-radius:50%;background:#111;border:3px solid var(--white)}
.cf{position:absolute;background:var(--white);height:34px;font-size:13px;font-style:italic;color:#666;padding:9px 12px}
.send{position:absolute;left:324px;top:262px;width:134px;height:36px;background:#111;color:var(--white);font-style:italic;font-size:15px;line-height:36px;text-align:center}
.office{position:absolute;top:306px;color:var(--white);font-size:13px;line-height:17px}
.office h5{font-size:17px;font-weight:700;text-decoration:underline;margin-bottom:8px}
.office .row{display:flex;gap:10px;align-items:flex-start;margin-bottom:6px}

/* footer */
.site-footer{position:absolute;left:0;top:3028px;width:1200px;height:102px;background:linear-gradient(#262626,#121212);color:var(--white)}
.foot-nav{position:absolute;left:140px;top:24px;display:flex;gap:28px;font-size:14px}
.copyright{position:absolute;left:140px;top:56px;font-size:13px}
.site-footer .brand{left:830px;top:12px;font-size:34px}
.site-footer .brand-dot{width:34px;height:34px}
.socials{position:absolute;left:890px;top:62px;display:flex;gap:6px}
.socials i{width:24px;height:24px;background:var(--white);border-radius:3px;display:block}
</style>
</head>
<body>

<header class="site-header">
  <div class="brand"><span class="brand-dot"></span>HostQubit</div>
  <div class="top-links">
    <span><svg width="14" height="14" viewBox="0 0 14 14"><circle cx="7" cy="4" r="3" fill="#fff"/><path d="M1 14a6 6 0 0 1 12 0z" fill="#fff"/></svg>My Account</span>
    <span><svg width="14" height="14" viewBox="0 0 14 14"><circle cx="7" cy="7" r="7" fill="#fff"/><path d="M4 3l2 2-1 1 3 3 1-1 2 2-2 1C6 10 4 8 3 5z" fill="#222"/></svg>+1 800 555 0142</span>
  </div>
  <nav class="main-nav">
    <a class="active" href="#">Home</a><a href="#">About Us</a><a href="#">Services</a><a href="#">Features</a><a href="#">Contact Us</a><a href="#">Support</a>
  </nav>
</header>

<section class="hero">
  <div class="hero-photo" role="img" aria-label="Engineer working at a laptop in a server room"></div>
  <p class="hero-tagline">we provide a great service at great prices to<br>help your business succeed online</p>
  <div class="slider-dots"><i class="on"></i><i></i><i></i><i></i></div>
</section>

<section class="quote-band">
  <div class="quote-avatar" role="img" aria-label="Customer portrait"></div>
  <p class="quote-text">“Lorem ipsum dolor sit amet, consectetuer The adipiscing elit, sed diam nonummy nibh Lorem euismod tincidunt ut laoreet. Lorem ipsum dolor sit amet.”</p>
  <p class="quote-author">- Lorem ipsum</p>
</section>

<form class="enquiry">
  <div class="enquiry-head">QUICK ENQUIRY</div>
  <p>Lorem ipsum dolor sit amet, consectetuer The adipiscing elit, sed diam nonummy nibh Lorem euismod tincidunt ut laoreet.</p>
  <label>Name</label><div class="field"></div>
  <label>Email Address</label><div class="field"></div>
  <label>What are you interested in?</label>
  <div class="field select">Please Choose<b><svg width="10" height="8" viewBox="0 0 10 8"><path d="M0 0h10L5 8z" fill="#333"/></svg></b></div>
  <span class="submit">SUBMIT</span>
  <p class="foot">Lorem ipsum dolor sit amet, consectetuer</p>
</form>

<h2 class="section-title about-title">ABOUT US</h2>
<p class="about-copy">Lorem ipsum dolor sit amet, consectetuer The adipiscing elit, sed diam nonummy nibh Lorem euismod tincidunt ut laoreet. Lorem ipsum dolor sit amet, consectetuer. Lorem ipsum dolor sit amet, consectetuer The adipiscing elit, sed diam nonummy nibh Lorem euismod tincidunt ut laoreet. Lorem ipsum dolor sit amet, consectetuer. Lorem ipsum dolor sit amet, consectetuer The adipiscing elit, sed diam nonummy nibh Lorem euismod tincidunt ut laoreet. Lorem ipsum dolor sit amet, consectetuer. Lorem ipsum dolor sit amet, consectetuer The adipiscing elit, sed diam nonummy nibh Lorem euismod tincidunt ut laoreet. Lorem ipsum dolor sit amet, consectetuer.</p>
<ul class="about-list">
  <li>Lorem ipsum dolor sit amet, consectetuer The adipiscing elit, sed diam nonummy nibh</li>
  <li>Lorem ipsum dolor sit amet, consectetuer The adipiscing elit, sed diam nonummy nibh Lorem</li>
  <li>Lorem ipsum dolor sit amet, consectetuer The adipiscing elit, sed diam nonummy nibh Lorem euismod</li>
</ul>

<section class="services">
  <h2 class="section-title services-title">OUR SERVICES</h2>
  <div class="plans">
    <article class="plan">
      <h3>Budget VPS</h3><p class="ram"><b>256 MB</b> Guaranteed RAM</p>
      <ul><li>1 x 3.4 Ghz Cores</li><li>10 GB Raid-10 Storage</li><li>300 GB Bandwidth</li><li>PanelVM Control Panel</li><li class="act">59 second Activation</li></ul>
      <div class="plan-price"><small>FROM</small><span class="amt">$<b>10</b> /MONTH</span><span class="order">ORDER NOW</span><span class="cmp">Compare Budget Vps</span></div>
    </article>
    <article class="plan">
      <h3>Standard VPS</h3><p class="ram"><b>768 MB</b> Guaranteed RAM</p>
      <ul><li>2x 3.4 Ghz Cores</li><li>40 GB Raid-10 Storage</li><li>1000 GB Bandwidth</li><li>PanelVM Control Panel</li><li class="act">59 second Activation</li></ul>
      <div class="plan-price"><small>FROM</small><span class="amt">$<b>25</b> /MONTH</span><span class="order">ORDER NOW</span><span class="cmp">Compare Budget Vps</span></div>
    </article>
    <article class="plan">
      <h3>Extreme VPS</h3><p class="ram"><b>2048 MB</b> Guaranteed RAM</p>
      <ul><li>2x 3.4 Ghz Cores</li><li>40 GB Raid-10 Storage</li><li>1000 GB Bandwidth</li><li>PanelVM Control Panel</li><li class="act">59 second Activation</li></ul>
      <div class="plan-price"><small>FROM</small><span class="amt">$<b>40</b> /MONTH</span><span class="order">ORDER NOW</span><span class="cmp">Compare Budget Vps</span></div>
    </article>
    <article class="plan">
      <h3>Custom VPS</h3><p class="ram">Customize your RAM</p>
      <ul><li>Customize CPU</li><li>Customize Storage</li><li>Customize Bandwidth</li><li>PanelVM Control Panel</li><li class="act">59 second Activation</li></ul>
      <div class="plan-price"><small>FROM</small><span class="amt">$<b>10</b> /MONTH</span><span class="order">ORDER NOW</span><span class="cmp">Compare Budget Vps</span></div>
    </article>
  </div>
</section>

<section class="cta-bar">
  <p class="msg">Lorem ipsum dolor sit amet, consectetuer The</p>
  <p class="phone"><svg width="26" height="26" viewBox="0 0 14 14"><circle cx="7" cy="7" r="6.3" fill="none" stroke="#fff" stroke-width="1.2"/><path d="M4.5 3.5l1.6 1.6-.8.8 2.6 2.6.8-.8 1.6 1.6-1.4 1C6.6 10 4.2 7.6 3.6 5z" fill="#fff"/></svg>+1 800 555 0142</p>
  <span class="cta-btn">GET STARTED</span>
</section>

<h2 class="section-title features-title">VPS HOSTING FEATURES</h2>
<div class="feature-grid">
  <div class="feature"><svg width="100" height="70" viewBox="0 0 100 70"><path d="M22 66a18 18 0 0 1-2-36 26 26 0 0 1 50-6 20 20 0 0 1 10 42z" fill="#f8b400"/><circle cx="50" cy="42" r="14" fill="#fff"/><path d="M50 42l6-6" stroke="#f8b400" stroke-width="3"/></svg><h4>59 Second Activation</h4><p>Your virtual host will be activated<br><br>immediately after your first payment so you dont wait.</p></div>
  <div class="feature"><svg width="100" height="70" viewBox="0 0 100 70"><path d="M22 66a18 18 0 0 1-2-36 26 26 0 0 1 50-6 20 20 0 0 1 10 42z" fill="#f8b400"/><path d="M50 24l12 30H38z" fill="none" stroke="#fff" stroke-width="3"/></svg><h4>99.9% Uptime</h4><p>We guarantee your VPS will have an uptime of 99.9% and strive for 100%.</p></div>
  <div class="feature"><svg width="100" height="70" viewBox="0 0 100 70"><path d="M22 66a18 18 0 0 1-2-36 26 26 0 0 1 50-6 20 20 0 0 1 10 42z" fill="#f8b400"/><rect x="38" y="30" width="24" height="24" fill="#fff"/><path d="M43 42l5 5 9-10" stroke="#3a9a3a" stroke-width="3" fill="none"/></svg><h4>14 Day Moneyback Guarantee</h4><p>If your unhappy with the service within 14<br>days we'll refund your money! There are no contracts, its just a month to month service.</p></div>
  <div class="feature"><svg width="100" height="70" viewBox="0 0 100 70"><path d="M22 66a18 18 0 0 1-2-36 26 26 0 0 1 50-6 20 20 0 0 1 10 42z" fill="#f8b400"/><rect x="36" y="40" width="28" height="12" rx="2" fill="#fff"/><path d="M50 22v14m-6-6l6 6 6-6" stroke="#fff" stroke-width="3" fill="none"/></svg><h4>Full Root Access</h4><p>ust like having your own dedicated server but cheaper than ever. Even tun/tap is supported.</p></div>
  <div class="feature"><svg width="100" height="70" viewBox="0 0 100 70"><path d="M22 66a18 18 0 0 1-2-36 26 26 0 0 1 50-6 20 20 0 0 1 10 42z" fill="#f8b400"/><path d="M38 44v-6a12 12 0 0 1 24 0v6" stroke="#fff" stroke-width="3" fill="none"/><rect x="34" y="42" width="8" height="10" rx="2" fill="#fff"/><rect x="58" y="42" width="8" height="10" rx="2" fill="#fff"/></svg><h4>24/7/365 Support</h4><p>We're here 24/7, weekends, holidays, day and night to assist you.</p></div>
  <div class="feature"><svg width="100" height="70" viewBox="0 0 100 70"><path d="M22 66a18 18 0 0 1-2-36 26 26 0 0 1 50-6 20 20 0 0 1 10 42z" fill="#f8b400"/><circle cx="50" cy="42" r="15" fill="#2d6fc4"/><ellipse cx="50" cy="42" rx="6" ry="15" fill="none" stroke="#fff" stroke-width="1.5"/><path d="M35 42h30" stroke="#fff" stroke-width="1.5"/></svg><h4>Global Locations</h4><p>We have severs located all over the world for you to choose from. Check our <a>locations</a> page</p></div>
  <div class="feature"><svg width="100" height="70" viewBox="0 0 100 70"><path d="M22 66a18 18 0 0 1-2-36 26 26 0 0 1 50-6 20 20 0 0 1 10 42z" fill="#f8b400"/><circle cx="50" cy="42" r="12" fill="none" stroke="#fff" stroke-width="4"/><circle cx="50" cy="42" r="4" fill="#fff"/></svg><h4>Choice of operating systems</h4><p>ust like having your own dedicated server but cheaper than ever. Even tun/tap is supported.</p></div>
  <div class="feature"><svg width="100" height="70" viewBox="0 0 100 70"><path d="M22 66a18 18 0 0 1-2-36 26 26 0 0 1 50-6 20 20 0 0 1 10 42z" fill="#f8b400"/><circle cx="50" cy="42" r="13" fill="#fff"/><path d="M50 42l7-7" stroke="#222" stroke-width="3"/></svg><h4>CtrlDesk/HostMgr</h4><p>You can order CtrlDesk for $15 per month on any of our VPSs that have 1024MB or more of RAM. We will automatically install the latest version of CtrlDesk for you.</p></div>
  <div class="feature"><svg width="100" height="70" viewBox="0 0 100 70"><path d="M22 66a18 18 0 0 1-2-36 26 26 0 0 1 50-6 20 20 0 0 1 10 42z" fill="#f8b400"/><circle cx="50" cy="42" r="15" fill="#2d6fc4"/><ellipse cx="50" cy="42" rx="6" ry="15" fill="none" stroke="#fff" stroke-width="1.5"/><path d="M35 42h30" stroke="#fff" stroke-width="1.5"/></svg><h4>IP Adresses</h4><p>All plans include 1 x IPv4 address. Upto 10 Additional IPv4 addresses may be ordered. Beyond 10 you need to request via email with a detailed description. IPv6's addresses are also available at some of our data centers on request. Reverse DNS entries are available for all IPs.</p></div>
  <div class="feature"><svg width="100" height="70" viewBox="0 0 100 70"><path d="M22 66a18 18 0 0 1-2-36 26 26 0 0 1 50-6 20 20 0 0 1 10 42z" fill="#f8b400"/><circle cx="50" cy="42" r="9" fill="#fff"/><path d="M50 26v32M34 42h32M39 31l22 22M61 31L39 53" stroke="#fff" stroke-width="4"/><circle cx="50" cy="42" r="4" fill="#f8b400"/></svg><h4>Upgrades with no downtime</h4><p>On all our non KVM plans you can easily upgrade your ram, disk or CPU with no downtime at all KVM plans will require a quick reboot.</p></div>
</div>

<section class="contact">
  <div class="abs" style="inset:0" role="img" aria-label="Road map of the region behind the contact form"></div>
  <div class="contact-overlay"></div>
  <h2>CONTACT US</h2>
  <span class="close"><svg width="30" height="30" viewBox="0 0 30 30"><path d="M9 9l12 12M21 9L9 21" stroke="#fff" stroke-width="3"/></svg></span>
  <div class="cf" style="left:324px;top:58px;width:272px">Name</div>
  <div class="cf" style="left:628px;top:58px;width:272px">Email Address</div>
  <div class="cf" style="left:324px;top:102px;width:272px">Phone</div>
  <div class="cf" style="left:628px;top:102px;width:272px">Subject</div>
  <div class="cf" style="left:324px;top:146px;width:576px;height:100px">Message</div>
  <span class="send">Send Enquiry</span>
  <div class="office" style="left:326px">
    <h5>New Zealand</h5>
    <div class="row"><svg width="12" height="16" viewBox="0 0 12 16"><path d="M6 16S0 9 0 6a6 6 0 0 1 12 0c0 3-6 10-6 10z" fill="#fff"/><circle cx="6" cy="6" r="2" fill="#333"/></svg><span>Street Name, City Name<br>Zip Code 00000</span></div>
    <div class="row"><svg width="14" height="14" viewBox="0 0 14 14"><circle cx="7" cy="7" r="7" fill="#fff"/><path d="M4 3l2 2-1 1 3 3 1-1 2 2-2 1C6 10 4 8 3 5z" fill="#333"/></svg><span>+64 900 555 01</span></div>
  </div>
  <div class="office" style="left:740px">
    <h5>Australia</h5>
    <div class="row"><svg width="12" height="16" viewBox="0 0 12 16"><path d="M6 16S0 9 0 6a6 6 0 0 1 12 0c0 3-6 10-6 10z" fill="#fff"/><circle cx="6" cy="6" r="2" fill="#333"/></svg><span>Street Name, City Name<br>Zip Code 00000</span></div>
    <div class="row"><svg width="14" height="14" viewBox="0 0 14 14"><circle cx="7" cy="7" r="7" fill="#fff"/><path d="M4 3l2 2-1 1 3 3 1-1 2 2-2 1C6 10 4 8 3 5z" fill="#333"/></svg><span>+61 20 555 0199</span></div>
  </div>
</section>

<footer class="site-footer">
  <nav class="foot-nav"><span>Home</span><span>About Us</span><span>Services</span><span>Features</span><span>Contact Us</span><span>Support</span></nav>
  <p class="copyright">Copyright 2014 HostQubit. A division of Tidewell Limited All Rights Reserved</p>
  <div class="brand"><span class="brand-dot"></span>HostQubit</div>
  <div class="socials"><i></i><i></i><i></i><i></i></div>
</footer>

</body>
</html>
```